Box Design for Flooring product

***IMPORTANT: PLEASE READ THE DOCUMENT PROVIDED WITH THIS BRIEF CAREFULLY BEFORE ACCEPTING THIS PROJECT***
Need a creative design for the packaging of a flooring product. The packaging is two boxes: one holding 36 planks of flooring, and the other 7 planks of flooring. There are 4 colours for the flooring planks that need a box designed (for both the 36 plank box and 7 plank box). The boxes measures 92 cm x 16cm x 7cm (36 planks) and 92 cm x 16cm x 1.5cm (7 planks).
More details are provided in the requirements document attached with this brief. Also attaching other supporting documents with this brief mentioned in the document.
Need extra days to review
- Montserrat-Regular

```html
<!DOCTYPE html>
<html lang="en">
<head>
<meta charset="utf-8">
<title>Terravelle – Self Adhesive Vinyl Plank Carton Templates</title>
<link rel="stylesheet" href="https://fonts.googleapis.com/css2?family=Montserrat:wght@400;500;600;700&display=swap">
<style>
  :root {
    --box: #5e5446;
    --paper: #ffffff;
    --tag-ink: #3d352b;
    --heading: #5e5446;
    --muted: #8a7e6e;
    --rule: #cfc8bd;
  }
  * { margin: 0; padding: 0; box-sizing: border-box; }
  html, body { width: 900px; height: 1200px; overflow: hidden; background: var(--paper); }
  .sheet {
    position: relative; width: 900px; height: 1200px;
    font-family: 'Montserrat', sans-serif; color: var(--heading);
  }
  .defs { position: absolute; width: 0; height: 0; overflow: hidden; }
  .sheet-title, .shade-name {
    position: absolute; transform: translateX(-50%);
    font-weight: 600; font-size: 26px; letter-spacing: 0.34em;
    white-space: nowrap; line-height: 1; padding-left: 0.34em;
  }
  .sheet-title { left: 453px; top: 65px; }
  .carton { position: absolute; display: block; }
  .carton--36 { width: 383px; height: 195px; }
  .carton--7 { width: 343px; height: 135px; }
  .carton text, .brand-sign text { font-family: 'Montserrat', sans-serif; }
  .panel { fill: var(--box); }
  .ink { fill: var(--paper); }
  .tag-ink { fill: var(--tag-ink); }
  .gap { fill: var(--paper); }
  .tick { fill: none; stroke: var(--paper); stroke-width: 1; }
  .cert { fill: none; stroke: var(--rule); stroke-width: 0.8; }
  .brand-sign { position: absolute; left: 672px; top: 1140px; width: 215px; height: 48px; }
  .brand-sign .mark { fill: var(--heading); }
  .brand-sign .name { fill: var(--heading); }
  .brand-sign .tagline { fill: var(--muted); }
</style>
</head>
<body>
<div class="sheet">

  <svg class="defs" aria-hidden="true" focusable="false">
    <defs>
      <linearGradient id="tone-dark-brown" x1="0" y1="0" x2="1" y2="0">
        <stop offset="0" stop-color="#2e3a44"/><stop offset="0.45" stop-color="#3f2c22"/><stop offset="0.7" stop-color="#5a3d2c"/><stop offset="1" stop-color="#6e4b36"/>
      </linearGradient>
      <linearGradient id="tone-natural-oak" x1="0" y1="0" x2="1" y2="0">
        <stop offset="0" stop-color="#e9e6e0"/><stop offset="0.4" stop-color="#e2a35a"/><stop offset="0.7" stop-color="#d8994b"/><stop offset="1" stop-color="#e2b160"/>
      </linearGradient>
      <linearGradient id="tone-wash-grey" x1="0" y1="0" x2="1" y2="0">
        <stop offset="0" stop-color="#d9ab2a"/><stop offset="0.3" stop-color="#d8d4cf"/><stop offset="0.6" stop-color="#a6a29c"/><stop offset="1" stop-color="#8e8a84"/>
      </linearGradient>
      <linearGradient id="tone-white-oak" x1="0" y1="0" x2="1" y2="0">
        <stop offset="0" stop-color="#9a7448"/><stop offset="0.35" stop-color="#d9d8d4"/><stop offset="0.7" stop-color="#e4e4e1"/><stop offset="1" stop-color="#efefed"/>
      </linearGradient>

      <!-- installation panel, set upside down on the back face -->
      <symbol id="install-panel" overflow="visible">
        <rect class="cert" x="9" y="6" width="21" height="18" rx="1"/>
        <rect class="ink" x="296" y="11" width="6" height="6" transform="rotate(180 302 15)"/>
        <text class="ink" x="302" y="17" font-size="7.5" textLength="44" transform="rotate(180 302 15)" text-anchor="start">TERRAVELLE</text>
        <text class="ink" x="310" y="44" font-size="3.4" text-anchor="middle" transform="rotate(180 310 43)">Acclimatise planks for 48 hours before fitting.</text>
        <text class="ink" x="500" y="34" font-size="3.4" text-anchor="middle" transform="rotate(180 500 33)">Keep flat and dry.</text>
        <g role="img" aria-label="Twelve small step photographs showing how to lay the planks">
          <rect x="45" y="65" width="19" height="19" fill="#d7b98a"/>
          <rect x="90" y="65" width="19" height="19" fill="#e6e2dc"/>
          <rect x="135" y="65" width="19" height="19" fill="#c89a6a"/>
          <rect x="181" y="65" width="19" height="19" fill="#b5ada2"/>
          <rect x="227" y="65" width="19" height="19" fill="#d9a56b"/>
          <rect x="272" y="65" width="19" height="19" fill="#ebe8e3"/>
          <rect x="318" y="65" width="19" height="19" fill="#9c9a96"/>
          <rect x="363" y="65" width="19" height="19" fill="#d8b27a"/>
          <rect x="407" y="65" width="19" height="19" fill="#e3c27f"/>
          <rect x="452" y="65" width="19" height="19" fill="#efece8"/>
          <rect x="497" y="65" width="19" height="19" fill="#cfcac3"/>
          <rect x="542" y="65" width="19" height="19" fill="#e1b35c"/>
        </g>
        <g font-size="4" class="ink">
          <text x="69" y="84" transform="rotate(180 70 82)">12</text>
          <text x="114" y="84" transform="rotate(180 115 82)">11</text>
          <text x="159" y="84" transform="rotate(180 160 82)">10</text>
          <text x="205" y="84" transform="rotate(180 206 82)">9</text>
          <text x="251" y="84" transform="rotate(180 252 82)">8</text>
          <text x="296" y="84" transform="rotate(180 297 82)">7</text>
          <text x="342" y="84" transform="rotate(180 343 82)">6</text>
          <text x="387" y="84" transform="rotate(180 388 82)">5</text>
          <text x="431" y="84" transform="rotate(180 432 82)">4</text>
          <text x="476" y="84" transform="rotate(180 477 82)">3</text>
          <text x="521" y="84" transform="rotate(180 522 82)">2</text>
          <text x="566" y="84" transform="rotate(180 567 82)">1</text>
        </g>
        <g font-size="3.3" class="ink" text-anchor="middle">
          <text x="55" y="60" transform="rotate(180 55 59)">Wipe clean</text>
          <text x="100" y="60" transform="rotate(180 100 59)">Roll surface</text>
          <text x="145" y="60" transform="rotate(180 145 59)">Fit border</text>
          <text x="191" y="60" transform="rotate(180 191 59)">Cut plank</text>
          <text x="237" y="60" transform="rotate(180 237 59)">Stagger joints</text>
          <text x="282" y="60" transform="rotate(180 282 59)">Press firmly</text>
          <text x="328" y="60" transform="rotate(180 328 59)">Align edge</text>
          <text x="373" y="60" transform="rotate(180 373 59)">Peel backing</text>
          <text x="417" y="60" transform="rotate(180 417 59)">Mark line</text>
          <text x="462" y="60" transform="rotate(180 462 59)">Measure room</text>
          <text x="507" y="60" transform="rotate(180 507 59)">Clean floor</text>
          <text x="552" y="60" transform="rotate(180 552 59)">Check planks</text>
        </g>
        <text class="ink" x="302" y="95" font-size="4" text-anchor="middle" transform="rotate(180 302 93.5)">INSTALLATION INSTRUCTION</text>
      </symbol>

      <!-- large carton dieline, 36 planks -->
      <symbol id="carton-36-frame" overflow="visible">
        <path class="panel" d="M48 52 L52 6 Q53 0 59 0 H641 Q647 0 648 6 L652 52 Z"/>
        <rect class="panel" x="48" y="49" width="604" height="103"/>
        <rect class="panel" x="48" y="157" width="604" height="43"/>
        <rect class="panel" x="48" y="204" width="604" height="105"/>
        <rect class="panel" x="48" y="313" width="604" height="44"/>
        <rect class="panel" x="0" y="49" width="46" height="103" rx="3"/>
        <rect class="panel" x="0" y="157" width="46" height="43" rx="3"/>
        <rect class="panel" x="0" y="204" width="46" height="105" rx="3"/>
        <rect class="panel" x="0" y="313" width="46" height="44" rx="3"/>
        <rect class="panel" x="654" y="49" width="48" height="103" rx="3"/>
        <rect class="panel" x="654" y="157" width="48" height="43" rx="3"/>
        <rect class="panel" x="654" y="204" width="48" height="105" rx="3"/>
        <rect class="panel" x="654" y="313" width="48" height="44" rx="3"/>
        <use href="#install-panel" x="48" y="49"/>
        <rect class="ink" x="188" y="173" width="467" height="12"/>
        <rect class="ink" x="153" y="171" width="14" height="14" transform="rotate(180 160 178)"/>
        <text class="ink" x="117" y="183" font-size="13" text-anchor="middle" textLength="84" transform="rotate(180 117 178.5)">TERRAVELLE</text>
        <text class="ink" x="117" y="172.5" font-size="3.6" text-anchor="middle" textLength="84" transform="rotate(180 117 171)">PREMIUM FLOORS AND TILES</text>
        <rect class="ink" x="354" y="327" width="160" height="13"/>
        <text class="tag-ink" x="434" y="337.3" font-size="10" text-anchor="middle" textLength="154">36 PLANKS | 5M² PER PACK</text>
        <rect class="ink" x="538" y="328" width="10" height="10"/>
        <text class="ink" x="555" y="337.5" font-size="12.5" textLength="83">TERRAVELLE</text>
        <text class="ink" x="555" y="343.5" font-size="3.4" textLength="83">PREMIUM FLOORS AND TILES</text>
      </symbol>

      <symbol id="carton-36-cut" overflow="visible">
        <rect class="gap" x="46" y="309" width="610" height="4"/>
      </symbol>

      <!-- small carton dieline, 7 planks -->
      <symbol id="carton-7-frame" overflow="visible">
        <path class="panel" d="M11 16 L14 4 Q15 0 21 0 H607 Q613 0 614 4 L617 16 V125 H11 Z"/>
        <rect class="panel" x="619" y="12" width="9" height="113"/>
        <rect class="panel" x="11" y="128" width="606" height="120"/>
        <rect class="panel" x="0" y="128" width="9" height="5"/>
        <rect class="panel" x="0" y="241" width="9" height="5"/>
        <rect class="panel" x="619" y="128" width="9" height="5"/>
        <rect class="panel" x="619" y="241" width="9" height="5"/>
        <use href="#install-panel" x="11" y="14"/>
      </symbol>

      <!-- front face copy, shared by both sizes -->
      <symbol id="front-copy" overflow="visible">
        <polyline class="tick" points="231,217.5 233,219.5 236.5,214.5"/>
        <text class="ink" x="244" y="221" font-size="9">Easy to lay</text>
        <polyline class="tick" points="244,229.5 246,231.5 249.5,226.5"/>
        <text class="ink" x="257" y="233" font-size="9">Water resistance</text>
        <polyline class="tick" points="256,242.5 258,244.5 261.5,239.5"/>
        <text class="ink" x="269" y="246" font-size="9">Easy to clean</text>
        <polyline class="tick" points="269,254.5 271,256.5 274.5,251.5"/>
        <text class="ink" x="282" y="258" font-size="9">Ideal for Bathroom and Kitchen</text>
        <polyline class="tick" points="281,266.5 283,268.5 286.5,263.5"/>
        <text class="ink" x="294" y="270" font-size="9">Suitable for general domestic use</text>
        <rect class="ink" x="493" y="219" width="16" height="16"/>
        <text class="ink" x="517" y="235" font-size="17" textLength="121">TERRAVELLE</text>
        <text class="ink" x="517" y="241" font-size="4.6" textLength="121">PREMIUM FLOORS AND TILES</text>
        <text class="ink" x="490" y="255" font-size="8.5" font-weight="600" textLength="148">SELF ADHESIVE VINYL PLANK</text>
        <polygon class="ink" points="543,286 655,286 655,300 535,300"/>
      </symbol>
    </defs>
  </svg>

  <h1 class="sheet-title">TEMPLATE BOX</h1>

  <!-- Dark brown -->
  <svg class="carton carton--36" style="left:38px;top:165px" viewBox="0 0 702 357" role="group" aria-label="Dark Brown, 36 plank carton">
    <use href="#carton-36-frame"/>
    <polygon points="48,204 190,204 350,357 48,357" fill="url(#tone-dark-brown)" role="img" aria-label="Photo of a living room with dark brown plank flooring and a diagonal band of planks"/>
    <use href="#carton-36-cut"/>
    <use href="#front-copy"/>
    <text class="ink" x="327" y="297" font-size="10.5" textLength="154">36 PLANKS | 5M² PER PACK</text>
    <text class="tag-ink" x="597" y="296.8" font-size="9" font-weight="600" text-anchor="middle">DARK BROWN</text>
  </svg>
  <svg class="carton carton--7" style="left:58px;top:409px" viewBox="0 0 628 248" role="group" aria-label="Dark Brown, 7 plank carton">
    <use href="#carton-7-frame"/>
    <polygon points="11,128 183,128 278,248 11,248" fill="url(#tone-dark-brown)" role="img" aria-label="Photo of a living room with dark brown plank flooring and a diagonal band of planks"/>
    <use href="#front-copy" x="-37" y="-72"/>
    <text class="ink" x="295" y="224" font-size="10.5" textLength="149">7 PLANKS | 1M² PER PACK</text>
    <text class="tag-ink" x="560" y="224.8" font-size="9" font-weight="600" text-anchor="middle">DARK BROWN</text>
  </svg>
  <h2 class="shade-name" style="left:230px;top:568px">DARK BROWN</h2>

  <!-- Natural oak -->
  <svg class="carton carton--36" style="left:483px;top:165px" viewBox="0 0 702 357" role="group" aria-label="Natural Oak, 36 plank carton">
    <use href="#carton-36-frame"/>
    <polygon points="48,204 190,204 350,357 48,357" fill="url(#tone-natural-oak)" role="img" aria-label="Photo of a bright hallway with natural oak plank flooring and a diagonal band of planks"/>
    <use href="#carton-36-cut"/>
    <use href="#front-copy"/>
    <text class="ink" x="327" y="297" font-size="10.5" textLength="154">36 PLANKS | 5M² PER PACK</text>
    <text class="tag-ink" x="597" y="296.8" font-size="9" font-weight="600" text-anchor="middle">NATURAL OAK</text>
  </svg>
  <svg class="carton carton--7" style="left:503px;top:409px" viewBox="0 0 628 248" role="group" aria-label="Natural Oak, 7 plank carton">
    <use href="#carton-7-frame"/>
    <polygon points="11,128 183,128 278,248 11,248" fill="url(#tone-natural-oak)" role="img" aria-label="Photo of a bright hallway with natural oak plank flooring and a diagonal band of planks"/>
    <use href="#front-copy" x="-37" y="-72"/>
    <text class="ink" x="295" y="224" font-size="10.5" textLength="149">7 PLANKS | 1M² PER PACK</text>
    <text class="tag-ink" x="560" y="224.8" font-size="9" font-weight="600" text-anchor="middle">NATURAL OAK</text>
  </svg>
  <h2 class="shade-name" style="left:675px;top:568px">NATURAL OAK</h2>

  <!-- Wash grey -->
  <svg class="carton carton--36" style="left:38px;top:679px" viewBox="0 0 702 357" role="group" aria-label="Wash Grey, 36 plank carton">
    <use href="#carton-36-frame"/>
    <polygon points="48,204 190,204 350,357 48,357" fill="url(#tone-wash-grey)" role="img" aria-label="Photo of a bedroom with yellow curtains and wash grey plank flooring with a diagonal band of planks"/>
    <use href="#carton-36-cut"/>
    <use href="#front-copy"/>
    <text class="ink" x="327" y="297" font-size="10.5" textLength="154">36 PLANKS | 5M² PER PACK</text>
    <text class="tag-ink" x="597" y="296.8" font-size="9" font-weight="600" text-anchor="middle">WASH GREY</text>
  </svg>
  <svg class="carton carton--7" style="left:58px;top:923px" viewBox="0 0 628 248" role="group" aria-label="Wash Grey, 7 plank carton">
    <use href="#carton-7-frame"/>
    <polygon points="11,128 183,128 278,248 11,248" fill="url(#tone-wash-grey)" role="img" aria-label="Photo of a bedroom with yellow curtains and wash grey plank flooring with a diagonal band of planks"/>
    <use href="#front-copy" x="-37" y="-72"/>
    <text class="ink" x="295" y="224" font-size="10.5" textLength="149">7 PLANKS | 1M² PER PACK</text>
    <text class="tag-ink" x="560" y="224.8" font-size="9" font-weight="600" text-anchor="middle">WASH GREY</text>
  </svg>
  <h2 class="shade-name" style="left:230px;top:1081px">WASH GREY</h2>

  <!-- White oak -->
  <svg class="carton carton--36" style="left:483px;top:679px" viewBox="0 0 702 357" role="group" aria-label="White Oak, 36 plank carton">
    <use href="#carton-36-frame"/>
    <polygon points="48,204 190,204 350,357 48,357" fill="url(#tone-white-oak)" role="img" aria-label="Photo of a wooden chair on white oak plank flooring with a diagonal band of planks"/>
    <use href="#carton-36-cut"/>
    <use href="#front-copy"/>
    <text class="ink" x="327" y="297" font-size="10.5" textLength="154">36 PLANKS | 5M² PER PACK</text>
    <text class="tag-ink" x="597" y="296.8" font-size="9" font-weight="600" text-anchor="middle">WHITE OAK</text>
  </svg>
  <svg class="carton carton--7" style="left:503px;top:923px" viewBox="0 0 628 248" role="group" aria-label="White Oak, 7 plank carton">
    <use href="#carton-7-frame"/>
    <polygon points="11,128 183,128 278,248 11,248" fill="url(#tone-white-oak)" role="img" aria-label="Photo of a wooden chair on white oak plank flooring with a diagonal band of planks"/>
    <use href="#front-copy" x="-37" y="-72"/>
    <text class="ink" x="295" y="224" font-size="10.5" textLength="149">7 PLANKS | 1M² PER PACK</text>
    <text class="tag-ink" x="560" y="224.8" font-size="9" font-weight="600" text-anchor="middle">WHITE OAK</text>
  </svg>
  <h2 class="shade-name" style="left:675px;top:1082px">WHITE OAK</h2>

  <svg class="brand-sign" viewBox="0 0 215 48" role="img" aria-label="Terravelle, premium floors and tiles">
    <rect class="mark" x="1" y="6" width="36" height="36"/>
    <text class="name" x="52" y="30" font-size="24" textLength="161">TERRAVELLE</text>
    <text class="tagline" x="52" y="42" font-size="7.2" textLength="161">PREMIUM FLOORS AND TILES</text>
  </svg>

</div>
</body>
</html>
```